Corvid Lens Studio Business Card Design

I need a business card designed for a photography business based in Perth, Western Australia called Corvid Lens Studio.

We specialise in wedding, event photography and portrait photography.

The business card must borrow the style of the attached logo.

The hex codes for the colours in the logo are:
#ED1D85 - Pink
#89C23E - Green
#37282F - Black

The name on the card will be:
Name: Tobiah
Phone: 0417395268
Website: www.corvidlensstudio.com.au
Friendsphere: corvidlensstudio

I am open and happy to accept creative concepts.

Industry/Entity Type

Business

```html
<!DOCTYPE html>
<html lang="en">
<head>
<meta charset="utf-8">
<title>Corvid Lens Studio – Business Card</title>
<link rel="stylesheet" href="https://fonts.googleapis.com/css2?family=Questrial&display=swap">
<style>
  :root {
    --pink: #ED1D85;
    --green: #89C23E;
    --ink: #37282F;
    --grey-text: #4a4a4a;
    --card: #ffffff;
    --stage-centre: #2c2c2c;
    --stage-edge: #000000;
    --smoke-rose: rgba(196, 120, 120, 0.22);
    --smoke-grey: rgba(170, 160, 160, 0.18);
  }
  * { margin: 0; padding: 0; box-sizing: border-box; }
  html, body { width: 1200px; height: 761px; overflow: hidden; }
  body {
    position: relative;
    background: radial-gradient(ellipse 55% 70% at 50% 50%, var(--stage-centre) 0%, #151515 55%, var(--stage-edge) 100%);
    font-family: "Questrial", "Century Gothic", sans-serif;
  }
  .card {
    position: absolute;
    background: var(--card);
    overflow: hidden;
  }
  .card--front { left: 348px; top: 62px; width: 509px; height: 305px; }
  .card--back  { left: 350px; top: 379px; width: 506px; height: 303px; }

  .smoke {
    position: absolute;
    inset: 0;
  }
  .card--front .smoke {
    background:
      linear-gradient(160deg, transparent 8%, var(--smoke-grey) 22%, transparent 40%),
      linear-gradient(200deg, transparent 20%, var(--smoke-rose) 38%, transparent 55%),
      linear-gradient(15deg, var(--smoke-grey) 0%, transparent 30%);
  }
  .card--back .smoke {
    background:
      linear-gradient(170deg, transparent 20%, var(--smoke-rose) 35%, transparent 52%),
      linear-gradient(190deg, transparent 40%, var(--smoke-grey) 60%, transparent 80%);
  }

  .mark {
    position: absolute;
    width: 64px;
    height: 64px;
    border-radius: 50%;
    background: var(--pink);
  }
  .card--front .mark { left: 223px; top: 103px; }
  .card--back .mark  { left: 220px; top: 34px; }

  .brand-line {
    position: absolute;
    left: 0; right: 0;
    top: 191px;
    padding-left: 102px;
    font-size: 13px;
    letter-spacing: 6.2px;
    color: var(--grey-text);
    text-transform: uppercase;
  }

  .holder-name {
    position: absolute;
    left: 0; right: 0;
    top: 107px;
    text-align: center;
    font-size: 23px;
    font-variant: small-caps;
    letter-spacing: 1px;
    color: var(--ink);
  }
  .website {
    position: absolute;
    left: 0; right: 0;
    top: 140px;
    text-align: center;
    font-size: 16px;
    letter-spacing: 1.6px;
    color: var(--grey-text);
    text-transform: uppercase;
  }
  .swoosh {
    position: absolute;
    left: 56px; top: 160px;
    width: 400px; height: 40px;
  }
  .contact {
    position: absolute;
    left: 62px;
    display: flex;
    align-items: center;
    gap: 16px;
    color: var(--ink);
  }
  .contact--phone { top: 198px; font-size: 18px; letter-spacing: 2.2px; }
  .contact--social { top: 236px; font-size: 15.5px; }
  .contact .icon { width: 28px; height: 28px; flex: none; }
</style>
</head>
<body>
  <section class="card card--front" aria-label="Card front">
    <div class="smoke" role="img" aria-label="Flowing translucent rose and grey smoke ribbons"></div>
    <div class="mark" aria-hidden="true"></div>
    <p class="brand-line">Corvid Lens Studio</p>
  </section>

  <section class="card card--back" aria-label="Card back">
    <div class="smoke" role="img" aria-label="Flowing translucent rose and grey smoke ribbons"></div>
    <div class="mark" aria-hidden="true"></div>
    <h1 class="holder-name">Tobiah</h1>
    <p class="website">www.corvidlensstudio.com.au</p>
    <svg class="swoosh" viewBox="0 0 400 40" aria-hidden="true">
      <path d="M2 26 C 60 4, 140 2, 230 14 C 300 24, 360 34, 398 30 C 350 40, 290 34, 230 22 C 150 8, 70 10, 2 26 Z" fill="#000"/>
    </svg>
    <div class="contact contact--phone">
      <svg class="icon" viewBox="0 0 24 24" aria-hidden="true">
        <path fill="var(--green)" d="M6.6 10.8a15.1 15.1 0 0 0 6.6 6.6l2.2-2.2a1 1 0 0 1 1-.25 11.4 11.4 0 0 0 3.6.57 1 1 0 0 1 1 1V20a1 1 0 0 1-1 1A17 17 0 0 1 3 4a1 1 0 0 1 1-1h3.5a1 1 0 0 1 1 1c0 1.25.2 2.45.57 3.57a1 1 0 0 1-.25 1z"/>
      </svg>
      <span>0417 395 268</span>
    </div>
    <div class="contact contact--social">
      <svg class="icon" viewBox="0 0 28 28" aria-hidden="true">
        <circle cx="14" cy="14" r="14" fill="var(--pink)"/>
      </svg>
      <span>www.friendsphere.com/corvidlensstudio</span>
    </div>
  </section>
</body>
</html>
```